Square Business Cards for Our Restaurant / Event Venue

We need square business cards designed for the management team of our event venue and restaurant. On one side of the card should be the the Harbor Lantern 7 logo and URL www.harborlantern7.example. On the other side should be the Ember Logo and URL www.emberhall7.example. All employee details should be on the side with Ember logo. There will be a total of 5 cards to be created with the design.

Clara Bennquist
clara@harborlantern7.example

main 555.418.3072
direct 555.730.2946

4831 West Orchard Lane SE
Washington, DC 90417

Industry/Entity Type

Business

```html
<!DOCTYPE html>
<html lang="en">
<head>
<meta charset="utf-8">
<title>Harbor Lantern 7 — Square Business Cards</title>
<link href="https://fonts.googleapis.com/css2?family=Open+Sans:ital,wght@0,400;0,600;0,700;1,700&display=swap" rel="stylesheet">
<style>
  :root {
    --backdrop: #3a3a3a;
    --card-white: #ffffff;
    --brand-red: #b83035;
    --ink: #2b2b2b;
    --on-red: #ffffff;
  }
  * { margin: 0; padding: 0; box-sizing: border-box; }
  html, body { width: 1200px; height: 801px; overflow: hidden; }
  body {
    background: var(--backdrop);
    font-family: "Open Sans", Arial, sans-serif;
    position: relative;
  }
  .card {
    position: absolute;
    top: 236px;
    width: 330px;
    height: 330px;
    overflow: hidden;
  }
  .card--front { left: 231px; background: var(--card-white); }
  .card--back { left: 641px; background: var(--brand-red); }

  .front-badge {
    position: absolute;
    left: 39px; top: 6px;
    width: 250px; height: 250px;
    border-radius: 50%;
    background: var(--brand-red);
    display: flex; align-items: center; justify-content: center;
  }
  .front-badge__name {
    color: var(--on-red);
    font-weight: 400;
    font-size: 29px;
    line-height: 1.15;
    text-align: center;
  }
  .front-url {
    position: absolute;
    left: 0; right: 0; top: 275px;
    text-align: center;
    font-weight: 700; font-style: italic;
    font-size: 14px;
    color: var(--ink);
  }

  .back-badge {
    position: absolute;
    left: 62px; top: -39px;
    width: 206px; height: 206px;
    border-radius: 50%;
    background: var(--card-white);
  }
  .back-badge__name {
    position: absolute;
    left: 0; right: 0; top: 62px;
    text-align: center;
    font-weight: 700;
    font-size: 46px;
    color: var(--ink);
  }
  .back-badge__url {
    position: absolute;
    left: 0; right: 0; top: 120px;
    text-align: center;
    font-weight: 700; font-style: italic;
    font-size: 13px;
    color: var(--ink);
  }
  .staff-name {
    position: absolute;
    left: 50px; top: 186px;
    font-weight: 700;
    font-size: 14px;
    color: var(--on-red);
    letter-spacing: 0.2px;
  }
  .contact-list {
    position: absolute;
    left: 28px; top: 212px;
    list-style: none;
    color: var(--on-red);
    font-weight: 700; font-style: italic;
    font-size: 13.5px;
    line-height: 20.5px;
  }
  .contact-list li { display: flex; align-items: flex-start; }
  .contact-list .icon {
    width: 13px; height: 13px;
    margin: 4px 9px 0 0;
    flex: none;
  }
  .contact-list .icon--blank { visibility: hidden; }
  .contact-list .group { display: flex; flex-direction: column; }
</style>
</head>
<body>
  <section class="card card--front">
    <div class="front-badge">
      <p class="front-badge__name">Harbor<br>Lantern 7</p>
    </div>
    <p class="front-url">www.harborlantern7.example</p>
  </section>

  <section class="card card--back">
    <div class="back-badge">
      <p class="back-badge__name">Ember</p>
      <p class="back-badge__url">www.emberhall7.example</p>
    </div>

    <p class="staff-name">CLARA BENNQUIST</p>

    <ul class="contact-list">
      <li>
        <svg class="icon" viewBox="0 0 14 14" aria-hidden="true"><circle cx="7" cy="7" r="6.5" fill="#fff"/><rect x="3.5" y="4.8" width="7" height="4.6" fill="none" stroke="#b83035" stroke-width="1"/><path d="M3.5 4.8 L7 7.6 L10.5 4.8" fill="none" stroke="#b83035" stroke-width="1"/></svg>
        <span>clara@harborlantern7.example</span>
      </li>
      <li>
        <svg class="icon" viewBox="0 0 14 14" aria-hidden="true"><circle cx="7" cy="7" r="6.5" fill="#fff"/><path d="M4.3 4 h1.6 l0.7 1.8 -0.9 0.7 a5 5 0 0 0 1.8 1.8 l0.7 -0.9 1.8 0.7 v1.6 a1 1 0 0 1 -1 1 A6 6 0 0 1 3.3 5 a1 1 0 0 1 1 -1z" fill="#b83035"/></svg>
        <span class="group"><span>main 555.418.3072</span><span>direct 555.730.2946</span></span>
      </li>
      <li>
        <svg class="icon" viewBox="0 0 14 14" aria-hidden="true"><circle cx="7" cy="7" r="6.5" fill="#fff"/><path d="M7 2.8 a3 3 0 0 1 3 3 c0 2.2 -3 5.4 -3 5.4 s-3 -3.2 -3 -5.4 a3 3 0 0 1 3 -3z" fill="#b83035"/><circle cx="7" cy="5.8" r="1.1" fill="#fff"/></svg>
        <span class="group"><span>4831 West Orchard Lane SE</span><span>Washington, DC 90417</span></span>
      </li>
    </ul>
  </section>
</body>
</html>
```